The amber lantern with an elephant incorporated in the background

Target Market(s)

Real estate

Industry/Entity Type

Real Estate

Contact Information for Business Card

On back on want my name & number
In front I want the business name, "the amber lantern", below to say staging & design

Logo Text

The amber lantern

Font styles to use
Serif

Colors
000000

Requirements
Must have
• I want an elephant behind the writing in gold transperant

```html
<!DOCTYPE html>
<html lang="en">
<head>
<meta charset="utf-8">
<title>The Amber Lantern – Business Card</title>
<link href="https://fonts.googleapis.com/css2?family=Jost:wght@400;500&family=Josefin+Sans:wght@300;400&display=swap" rel="stylesheet">
<style>
  :root {
    --backdrop: #ecebe8;
    --card: #ffffff;
    --ink: #111111;
    --gold: #c9bd2e;
    --gold-soft: rgba(201, 189, 46, 0.35);
    --shadow: rgba(0, 0, 0, 0.12);
  }
  * { margin: 0; padding: 0; box-sizing: border-box; }
  html, body {
    width: 1200px;
    height: 804px;
    overflow: hidden;
    background: var(--backdrop);
  }
  .sheet {
    position: relative;
    width: 1200px;
    height: 804px;
    display: flex;
    align-items: center;
    justify-content: center;
    gap: 40px;
  }
  .card {
    position: relative;
    width: 540px;
    height: 310px;
    background: var(--card);
    border-radius: 18px;
    box-shadow: 0 6px 20px var(--shadow);
    overflow: hidden;
  }

  /* Front */
  .brand-mark {
    position: absolute;
    left: 282px;
    top: 48px;
    width: 150px;
    height: 150px;
    border-radius: 50%;
    background: var(--gold-soft);
  }
  .brand-name {
    position: absolute;
    left: 0;
    right: 0;
    top: 132px;
    text-align: center;
    font-family: "Jost", sans-serif;
    font-weight: 500;
    font-size: 38px;
    letter-spacing: 1px;
    color: var(--ink);
    text-transform: uppercase;
  }
  .brand-tagline {
    position: absolute;
    left: 0;
    right: 0;
    top: 184px;
    text-align: center;
    font-family: "Josefin Sans", sans-serif;
    font-weight: 300;
    font-size: 16px;
    letter-spacing: 1px;
    color: var(--ink);
  }

  /* Back */
  .contact-strip {
    position: absolute;
    left: 0;
    top: 0;
    width: 30px;
    height: 200px;
    background: var(--gold);
    border-bottom-right-radius: 6px;
  }
  .contact-icons {
    position: absolute;
    left: 5px;
    top: 112px;
    display: flex;
    flex-direction: column;
    gap: 8px;
  }
  .contact-icons svg { display: block; }
  .contact-details {
    position: absolute;
    left: 46px;
    top: 130px;
    font-family: "Josefin Sans", sans-serif;
    font-weight: 300;
    color: var(--ink);
    line-height: 1.9;
  }
  .contact-phone { font-size: 17px; letter-spacing: 1px; }
  .contact-email { font-size: 12px; }
  .holder {
    position: absolute;
    right: 70px;
    top: 54px;
    text-align: center;
    color: var(--ink);
  }
  .holder-name {
    font-family: "Jost", sans-serif;
    font-weight: 400;
    font-size: 24px;
    letter-spacing: 1px;
  }
  .holder-role {
    font-family: "Josefin Sans", sans-serif;
    font-weight: 300;
    font-size: 12px;
    margin-top: 4px;
  }
  .skyline {
    position: absolute;
    right: 0;
    bottom: 0;
    width: 330px;
    height: 150px;
  }
</style>
</head>
<body>
<main class="sheet">
  <section class="card card-front" aria-label="Card front">
    <div class="brand-mark" aria-hidden="true"></div>
    <h1 class="brand-name">The Amber Lantern</h1>
    <p class="brand-tagline">staging &amp; design</p>
  </section>

  <section class="card card-back" aria-label="Card back">
    <div class="contact-strip">
      <div class="contact-icons">
        <svg width="20" height="20" viewBox="0 0 20 20" aria-hidden="true">
          <path d="M10 3 L3 9 H5 V16 H8.5 V12 H11.5 V16 H15 V9 H17 Z" fill="#ffffff"/>
        </svg>
        <svg width="20" height="20" viewBox="0 0 20 20" aria-hidden="true">
          <path d="M6 3 L8.5 6.5 L7 8.5 Q9 12 11.5 13 L13.5 11.5 L17 14 L15.5 16.5 Q9 17 5 11 Q3 7 3.5 4.5 Z" fill="#ffffff"/>
        </svg>
        <svg width="20" height="20" viewBox="0 0 20 20" aria-hidden="true">
          <rect x="3" y="5" width="14" height="10" rx="1.5" fill="#ffffff"/>
          <path d="M3.5 5.5 L10 11 L16.5 5.5" fill="none" stroke="#c9bd2e" stroke-width="1.4"/>
        </svg>
      </div>
    </div>
    <div class="contact-details">
      <p class="contact-phone">01632 960418</p>
      <p class="contact-email">theamberlantern@mailbox.com</p>
    </div>
    <div class="holder">
      <p class="holder-name">YOUR NAME</p>
      <p class="holder-role">Designation</p>
    </div>
    <div class="skyline" role="img" aria-label="Sketched city skyline in gold"
         style="background: linear-gradient(160deg, rgba(201,189,46,0) 30%, rgba(201,189,46,0.75) 70%, #c9bd2e 100%);"></div>
  </section>
</main>
</body>
</html>
```